Dog Snacks brand needs a new packaging design

Dear Designers,

We are looking for a packaging expert to design our new line of Dog Snacks which contain a relaxing hemp extract (CBD).

Our company is already selling various relaxing cat & dog products , and we would like this new design to reflect the same "style & feeling" as our current products (see attached instructions).

Technical aspects:
- The packaging is a Stand Up Pouch (12x18.5x7cm - see attached instructions).
- Please follow technical guidelines from printer (see attached instructions).
- The packaging will contain 120g of high-quality, semi-moist dog snacks.
- We will be designing 3 differents variations for 3 different flavours: Chicken, Beef & Liver.
- The packaging will be printed with a matt finish.

Design aspects:
- The design should be compatible with our brand identity (i.e. fluffly, pure, relaxing, positive, clean & natural).
- Soft/rounded shapes are preferred.
- Please use our brand's colors (#3BA384, White & Black).
- Please use our company logo (see attached instructions).
- The design also needs to convey a strong sense of professionalism as we are an animal "healthcare" brand.
- If you want to include a dog picture, we would prefer you to use a picture of our official brand ambassador (see attached instructions).
- We have attached a number of packaging examples which we like a lot. (see attached instructions). Please only use those as general inspiration.
- Only original work (no plagiarism will be accepted).

Please don't hesitate to send us a message if you have any questions about the brand, the product or the design requirements.

We look forward to seeing your designs & working on this together !

Thanks & regards,
Marcus

Dog owners

Pet Care

Sans Serif

• Please see project description.

```html
<!DOCTYPE html>
<html lang="en">
<head>
<meta charset="utf-8">
<title>VerdaBites CBD Treats – Pouch Front and Back</title>
<link href="https://fonts.googleapis.com/css2?family=Arvo:wght@400;700&family=Josefin+Sans:wght@400;600&display=swap" rel="stylesheet">
<style>
  :root {
    --brand-green: #3ba384;
    --deep-green: #1f7d60;
    --stage-green: #158264;
    --paper: #ffffff;
    --ink: #141414;
    --soft-grey: #e9eeec;
  }
  * { box-sizing: border-box; margin: 0; padding: 0; }
  html, body { width: 1200px; height: 814px; overflow: hidden; }
  body { background: var(--stage-green); position: relative; font-family: "Arvo", serif; }

  .pouch {
    position: absolute; top: 110px; width: 330px; height: 575px;
    background: var(--paper); border-radius: 14px 14px 8px 8px; overflow: hidden;
  }
  .pouch--front { left: 300px; }
  .pouch--back { left: 695px; }

  .pouch__top-band { position: absolute; left: 0; top: 70px; width: 330px; height: 60px; }

  .brand { position: absolute; left: 0; width: 100%; text-align: center; }
  .brand__name { font-family: "Josefin Sans", sans-serif; font-weight: 400; color: var(--ink); letter-spacing: 1px; }
  .brand__tag { font-family: "Josefin Sans", sans-serif; color: var(--brand-green); }

  .pouch--front .brand { top: 168px; }
  .pouch--front .brand__name { font-size: 34px; }
  .pouch--front .brand__tag { font-size: 13px; margin-left: 118px; margin-top: -4px; }

  .product-name {
    position: absolute; left: 40px; top: 250px; font-weight: 700; font-size: 40px;
    color: var(--deep-green); letter-spacing: -0.5px;
  }
  .product-name sup { font-size: 13px; font-weight: 400; vertical-align: 24px; margin-left: 2px; }
  .rule { position: absolute; height: 1px; background: #6b6b6b; }
  .rule--title { left: 40px; top: 300px; width: 300px; }
  .rule--benefits { left: 26px; top: 442px; width: 168px; background: var(--brand-green); }

  .dog-photo {
    position: absolute; left: 166px; top: 292px; width: 164px; height: 150px;
    background: radial-gradient(ellipse at 55% 55%, #f4f1ee 0%, #e4dfda 60%, #ffffff 100%);
    border-radius: 50% 40% 0 0;
  }

  .headline {
    position: absolute; left: 26px; top: 330px; font-weight: 700; font-size: 42px;
    line-height: 43px; color: var(--ink); letter-spacing: -0.5px;
  }
  .benefits {
    position: absolute; left: 26px; top: 423px; font-size: 11px; color: var(--deep-green);
    display: flex; gap: 6px; letter-spacing: 0.3px;
  }
  .benefits span::before { content: "▪ "; font-size: 8px; }

  .facts {
    position: absolute; left: 26px; top: 460px; display: flex; align-items: center; gap: 8px;
    color: var(--deep-green);
  }
  .facts__thc { font-weight: 700; font-size: 20px; }
  .fact { display: flex; align-items: center; gap: 4px; font-size: 9.5px; line-height: 11px; border-left: 1px solid var(--deep-green); padding-left: 7px; }
  .fact__icon { width: 14px; height: 14px; border-radius: 50%; background: var(--deep-green); flex: none; }
  .fact__icon--square { border-radius: 2px; }

  .pattern-band {
    position: absolute; left: 0; width: 100%; height: 58px;
    background: linear-gradient(180deg, #2f9776 0%, var(--brand-green) 100%);
  }
  .pouch--front .pattern-band { top: 500px; }
  .pouch--back .pattern-band { top: 504px; }

  .pouch--back .brand { top: 176px; }
  .pouch--back .brand__name { font-size: 20px; }
  .pouch--back .brand__tag { font-size: 8px; margin-left: 50px; margin-top: -2px; }

  .copy { position: absolute; left: 28px; width: 274px; text-align: center; color: var(--deep-green); font-size: 7.4px; line-height: 10px; }
  .copy h2 { font-size: 10.5px; font-weight: 400; color: var(--ink); margin-bottom: 2px; letter-spacing: 0.2px; }
  .copy p + p { margin-top: 8px; }
  .copy--intro { top: 204px; }
  .copy--storage { top: 302px; }
  .copy--ingredients { top: 350px; }

  .label-box { position: absolute; left: 40px; top: 428px; width: 90px; height: 58px; background: var(--deep-green); }
  .distributor { position: absolute; left: 148px; top: 432px; font-size: 8px; line-height: 11px; color: var(--deep-green); }
  .distributor strong { display: block; font-weight: 400; font-size: 10px; color: var(--ink); }
  .vet-badge {
    position: absolute; left: 238px; top: 424px; width: 56px; height: 56px; border-radius: 50%;
    border: 2px solid var(--brand-green); background: var(--soft-grey);
  }
</style>
</head>
<body>

  <section class="pouch pouch--front" aria-label="Pouch front">
    <svg class="pouch__top-band" viewBox="0 0 330 60" aria-hidden="true">
      <path d="M0 2 H140 Q160 2 165 50 Q170 2 190 2 H330 V10 H194 Q176 10 165 58 Q154 10 136 10 H0 Z" fill="var(--brand-green)"/>
    </svg>
    <div class="brand">
      <div class="brand__name">VERDALO</div>
      <div class="brand__tag">For Animals</div>
    </div>
    <div class="product-name">VerdaBites<sup>TM</sup></div>
    <div class="rule rule--title"></div>
    <div class="dog-photo" role="img" aria-label="Photo of the brand's white wrinkled dog ambassador in profile, wearing a light blue collar"></div>
    <h1 class="headline">CBD<br>TREATS</h1>
    <div class="benefits"><span>SUPPORT</span>|<span>CALM</span>|<span>EASE</span></div>
    <div class="rule rule--benefits"></div>
    <div class="facts">
      <span class="facts__thc">0%THC</span>
      <span class="fact"><span class="fact__icon"></span>Chicken<br>Flavour</span>
      <span class="fact"><span class="fact__icon fact__icon--square"></span>Net wt<br>120g</span>
      <span class="fact"><span class="fact__icon"></span>CBD<br>250mg</span>
    </div>
    <div class="pattern-band" role="img" aria-label="Band of white paw print pattern"></div>
  </section>

  <section class="pouch pouch--back" aria-label="Pouch back">
    <svg class="pouch__top-band" viewBox="0 0 330 60" aria-hidden="true">
      <path d="M0 2 H140 Q160 2 165 50 Q170 2 190 2 H330 V10 H194 Q176 10 165 58 Q154 10 136 10 H0 Z" fill="var(--brand-green)"/>
    </svg>
    <div class="brand">
      <div class="brand__name">VERDALO</div>
      <div class="brand__tag">For Animals</div>
    </div>
    <div class="copy copy--intro">
      <h2>GIVE THEM THE TREAT OF JOY:</h2>
      <p>Fear of abandonment, separation anxiety, phobias and behaviour problems can disturb your faithful companion's inner balance and peace of mind.</p>
      <p>VERDALO has specially formulated these CBD-infused treats so that your dog can live a more relaxing life.</p>
      <p>These treats are rich in poultry and vegetables, plus they taste just as good as the natural feeling of well-being and joy they bring!</p>
    </div>
    <div class="copy copy--storage">
      <h2>STORAGE &amp; WARNING:</h2>
      <p>Store at room temperature (15-25°C) in a cool, dry place away from light. Supplementary food exclusively for pets. If in doubt, consult your veterinarian.</p>
    </div>
    <div class="copy copy--ingredients">
      <h2>INGREDIENTS:</h2>
      <p>Meat and animal derivatives (20% poultry), cereals, derivatives of vegetable origin, hemp extract (0% THC). Analytical constituents: crude protein (31%), crude fat (5.5%), crude fibre (2%), crude ash (5%), moisture (25%).</p>
    </div>
    <div class="label-box"></div>
    <div class="distributor">
      <strong>Distributed by:</strong>
      VERDA TRADE KFT.<br>Lomb utca 14<br>1087 Budapest<br>Hungary
    </div>
    <div class="vet-badge"></div>
    <div class="pattern-band" role="img" aria-label="Band of white paw print pattern"></div>
  </section>

</body>
</html>
```